Specialized tax accounting firm needs marketing postcard

We need a postcard design for a professional services firm called R. Desmond Plork Inc. The firm is essentially a very specialized tax accounting firm - instead of serving the end consumer, we support other public accounting firms in the area of Canadian and U.S. tax advisory and compliance (i.e. they call us on tax issues too complex for the general practitioner). Our byline is "Tax Support Services for Public Accounting Firms". Our postcard should utilize our logo and be based on colours present in our logo (see file attached). The final design needs to convey professionalism and trustworthiness (we're hired by accountants after all!) while being creative and eye-catching. Eye-catching is critical, since many prospective recipients will not have heard from me before and I want them to read the postcard.

I've attached:
The font used in the logo
The logo itself in a variety of file formats
A picture of myself for incorporation in the postcard
A sample postcard from Publisher showing the wording to be used in the postcard and the elements to be included

Please note that in including a draft postcard I don't want the designer to follow the layout as is. It just shows the basic elements I want included. The only element which should remain constant is the wording - I do want the text elements included as written - however, everything else - font, size, placement of elements, etc. is up for creative ideas.

Please note that there is much more leather background around the logo than needs to be incorporated in the letterhead.

Industry/Entity Type

Accounting

```html
<!DOCTYPE html>
<html lang="en">
<head>
<meta charset="utf-8">
<title>R. Desmond Plork Inc. — Postcard</title>
<link rel="stylesheet" href="https://fonts.googleapis.com/css2?family=Cinzel:wght@400;500&display=swap">
<style>
  :root {
    --stage: #808184;
    --stage-edge: #ffffff;
    --card: #ffffff;
    --navy: #1e3d6b;
    --navy-text: #1c3566;
    --orange: #f2a23a;
    --purple: #5a3f8f;
    --sky: #2396d6;
    --leather-hi: #2c2c2c;
    --leather-lo: #0b0b0b;
    --white: #ffffff;
  }
  * { box-sizing: border-box; margin: 0; padding: 0; }
  html, body { width: 1200px; height: 914px; overflow: hidden; }
  body {
    position: relative;
    background: var(--stage);
    font-family: "Cinzel", "Times New Roman", serif;
  }
  .stage-edge { position: absolute; left: 0; top: 0; width: 17px; height: 914px; background: var(--stage-edge); }

  .card { position: absolute; top: 273px; width: 506px; height: 388px; overflow: hidden; }
  .card--back { left: 75px; background: var(--card); }
  .card--front { left: 632px; background: radial-gradient(ellipse at 55% 35%, var(--leather-hi), var(--leather-lo) 75%); }

  /* Back side */
  .brand-band {
    position: absolute; left: 0; top: 37px; width: 492px; height: 82px;
    background: var(--navy);
  }
  .brand-mark { position: absolute; background: var(--orange); }
  .brand-band .brand-mark { left: 18px; top: 13px; width: 60px; height: 60px; }
  .brand-name {
    position: absolute; color: var(--white); font-weight: 400; white-space: nowrap; line-height: 1;
  }
  .brand-band .brand-name { left: 92px; top: 9px; font-size: 36px; letter-spacing: 1px; }
  .brand-inc {
    position: absolute; color: var(--white); font-size: 11px; line-height: 1;
    display: flex; align-items: center; gap: 8px;
  }
  .brand-inc::before, .brand-inc::after { content: ""; height: 1px; background: var(--white); flex: 1; }
  .brand-band .brand-inc { left: 94px; top: 46px; width: 368px; }
  .brand-byline { position: absolute; color: var(--white); white-space: nowrap; line-height: 1; }
  .brand-band .brand-byline { left: 92px; top: 63px; font-size: 11.2px; letter-spacing: 0.3px; }

  .rule { position: absolute; left: 18px; width: 442px; height: 2px; background: var(--navy); }
  .rule--top { top: 140px; }
  .rule--bottom { top: 230px; }

  .about {
    position: absolute; left: 16px; top: 161px; width: 360px;
    color: var(--navy-text); font-size: 10.6px; line-height: 11.6px; letter-spacing: 0.2px;
  }

  .contact {
    position: absolute; left: 16px; top: 256px;
    color: var(--orange); font-size: 10.6px; line-height: 12.3px; letter-spacing: 0.2px;
  }
  .contact-invite { white-space: nowrap; margin-bottom: 2px; }
  .contact-list { list-style: none; }

  .write-lines { position: absolute; left: 190px; top: 280px; }

  /* Front side */
  .portrait {
    position: absolute; left: 272px; top: 36px; width: 190px; height: 276px;
    background: linear-gradient(180deg, #3a3430 0%, #1f1f22 45%, #141417 100%);
    border-radius: 80px 80px 0 0;
  }
  .front-panel {
    position: absolute; left: 258px; top: 312px; width: 215px; height: 76px;
    background: var(--sky); border-radius: 0 52px 0 0;
  }
  .front-brand .brand-mark { left: 84px; top: 314px; width: 46px; height: 46px; }
  .front-brand .brand-name { left: 140px; top: 313px; font-size: 27.5px; letter-spacing: 0.8px; }
  .front-brand .brand-inc { left: 140px; top: 338px; width: 282px; font-size: 9px; }
  .front-brand .brand-byline { left: 140px; top: 352px; font-size: 8.6px; letter-spacing: 0.2px; }
  .front-bar { position: absolute; left: 84px; top: 370px; width: 338px; height: 7px; background: var(--white); }
</style>
</head>
<body>
  <div class="stage-edge"></div>

  <section class="card card--back" aria-label="Postcard back">
    <div class="brand-band">
      <div class="brand-mark"></div>
      <div class="brand-name">R. DESMOND PLORK</div>
      <div class="brand-inc">INC</div>
      <div class="brand-byline">TAX SUPPORT SERVICES FOR PUBLIC ACCOUNTING FIRMS</div>
    </div>

    <div class="rule rule--top"></div>
    <p class="about">R. Desmond Plork Inc. is a boutique tax accounting firm specializing in tax support for public accounting firms. However, I also provide Canadian and U.S. tax advisory and compliance services to the general public.</p>
    <div class="rule rule--bottom"></div>

    <div class="contact">
      <p class="contact-invite">Please feel free to contact me if I can be of assistance to you or to your clients.</p>
      <ul class="contact-list">
        <li>Rowan D. Plork, CGA</li>
        <li>R. Desmond Plork Inc.</li>
        <li>18-410 Harbourview Lane</li>
        <li>Eastport, NS B2X 4K7</li>
        <li>(902) 555-0148</li>
        <li>rowan@plorktax.services</li>
        <li>www.plorktax.services</li>
      </ul>
    </div>

    <svg class="write-lines" width="286" height="70" viewBox="0 0 286 70" aria-hidden="true">
      <defs>
        <linearGradient id="lineTone" x1="0" x2="1">
          <stop offset="0" stop-color="#f2a23a"/>
          <stop offset="1" stop-color="#5a3f8f"/>
        </linearGradient>
      </defs>
      <g stroke="url(#lineTone)" stroke-width="1.2">
        <line x1="0" y1="1" x2="285" y2="1"/>
        <line x1="0" y1="14" x2="285" y2="14"/>
        <line x1="0" y1="27" x2="285" y2="27"/>
        <line x1="0" y1="40" x2="285" y2="40"/>
        <line x1="0" y1="54" x2="285" y2="54"/>
        <line x1="0" y1="67" x2="285" y2="67"/>
      </g>
    </svg>
  </section>

  <section class="card card--front" role="img" aria-label="Postcard front on a dark leather texture background">
    <div class="portrait" role="img" aria-label="Portrait photo of the firm's accountant in a dark suit with arms crossed"></div>
    <div class="front-panel"></div>
    <div class="front-brand">
      <div class="brand-mark"></div>
      <div class="brand-name">R. DESMOND PLORK</div>
      <div class="brand-inc">INC</div>
      <div class="brand-byline">TAX SUPPORT SERVICES FOR PUBLIC ACCOUNTING FIRMS</div>
    </div>
    <div class="front-bar"></div>
  </section>
</body>
</html>
```